Now Hiring Drivers or Help Wanted Ad

I am looking for an ad to be used for digital marketing for employment. Below is some or all of the information to work into the ad.

KORVA Holdings, LLC is a stable and premier hauler operating in the Northeast Wisconsin region since 1994. We have a variety of equipment from Dump Trucks, Roll Off Trucks to Semis with Belt Trailers, Walking Floors, Gondolas, Tankers, Vans and Compacting Trailers offering a variety of positions with different routes to mix up your day or settle into something you enjoy. We also offer low boy services and some flat bed work. We haul various materials from general aggregate freight to various types of non-hazardous wastes such as garbage, recyclables, paper mill sludge, metal, shredder fluff to various landfills or recycling centers.

Rate of pay is based on experience and the variety of equipment you are able to operate or your willingness to learn.

All work is local and you are home every night.

Great Pay
Sign on Bonus
Holiday & Vacation Pay
Health Insurance, Vision & Dental Offered
Employer Paid Life Insurance
Uniforms
Phone Reimbursement
PLUMEX

Industry/Entity Type

Trucking and Excavation

Colors
EB3D1F
EC4F4E
F09395
F8D3D4
FCEDEE

Requirements
Must have
• Should have some of the same look/feel of the ad attached.

```html
<!DOCTYPE html>
<html lang="en">
<head>
<meta charset="utf-8">
<title>KORVA Holdings – Hiring Drivers</title>
<link rel="stylesheet" href="https://fonts.googleapis.com/css2?family=Poppins:wght@300;400;600;700;800;900&display=swap">
<style>
  :root {
    --green: #4DB35E;
    --yellow: #F2C41B;
    --navy: #1E2B5E;
    --ink: #2B2B2B;
    --black: #000000;
    --white: #FFFFFF;
    --truck-red: #B8232A;
    --steel: #8C949C;
  }
  * { margin: 0; padding: 0; box-sizing: border-box; }
  html, body { width: 848px; height: 1200px; overflow: hidden; background: var(--white); }
  body { font-family: "Poppins", sans-serif; }
  .flyer { position: relative; width: 848px; height: 1200px; overflow: hidden; background: var(--white); }

  .hero-photo {
    position: absolute; left: 0; top: 0; width: 848px; height: 570px;
    background: linear-gradient(100deg, #9FA7AE 0%, #7D858D 14%, #C2262D 30%, #A81E25 55%, #D3363B 72%, #8E969E 88%, #B9C0C6 100%);
  }
  .shapes { position: absolute; left: 0; top: 0; }

  .headline { position: absolute; left: 268px; font-weight: 900; line-height: 1; letter-spacing: -5px; }
  .headline--hiring { top: 18px; color: var(--white); font-size: 150px; }
  .headline--drivers { top: 132px; color: var(--yellow); font-size: 142px; }

  .brand { position: absolute; left: 160px; top: 340px; width: 270px; text-align: center; }
  .brand__name { color: var(--green); font-weight: 800; font-size: 50px; line-height: 1; letter-spacing: 1px; }
  .brand__legal { color: var(--green); font-weight: 800; font-size: 13px; margin-top: 6px; letter-spacing: 1px; }
  .brand__place { color: var(--navy); font-weight: 700; font-size: 9px; margin-top: 3px; letter-spacing: 0.5px; }

  .equipment { position: absolute; left: 40px; top: 582px; width: 330px; }
  .equipment__title { color: var(--navy); font-weight: 700; font-size: 35px; line-height: 1.05; letter-spacing: -0.5px; }

  .bullets { list-style: none; }
  .bullets li { position: relative; color: var(--ink); font-weight: 600; }
  .bullets li::before { content: ""; position: absolute; border-radius: 50%; background: var(--green); }

  .equipment .bullets { margin-top: 12px; }
  .equipment .bullets li { padding-left: 39px; font-size: 17px; line-height: 23px; margin-bottom: 4px; }
  .equipment .bullets li::before { left: 4px; top: 5px; width: 14px; height: 14px; }

  .note { color: var(--ink); font-weight: 300; font-size: 15px; line-height: 20px; text-align: justify; }
  .equipment__note { position: absolute; left: 44px; top: 868px; width: 303px; }

  .perks { position: absolute; left: 436px; top: 490px; width: 380px; }
  .perks__title { font-size: 35px; font-weight: 300; color: var(--green); line-height: 1.1; letter-spacing: -0.5px; }
  .perks__title strong { color: var(--black); font-weight: 800; }
  .perks .bullets { margin-top: 10px; }
  .perks .bullets li { padding-left: 43px; font-size: 21px; line-height: 24px; margin-bottom: 8px; font-weight: 700; color: #333; }
  .perks .bullets li::before { left: 0; top: 5px; width: 16px; height: 16px; }
  .perks__note { position: absolute; left: 436px; width: 335px; }
  .perks__note--pay { top: 876px; }
  .perks__note--home { top: 956px; width: 296px; }

  .footer { position: absolute; left: 0; top: 1095px; width: 848px; height: 60px; }
  .footer__call { position: absolute; left: 36px; top: 5px; color: var(--white); font-weight: 700; font-size: 32px; letter-spacing: -1px; }
  .footer__social { position: absolute; left: 426px; top: 20px; color: var(--white); font-weight: 600; font-size: 12px; letter-spacing: 1.2px; }
  .footer__icons { position: absolute; left: 657px; top: 8px; display: flex; gap: 8px; }
  .footer__icon { width: 36px; height: 36px; border-radius: 50%; background: var(--green); display: flex; align-items: center; justify-content: center; }
</style>
</head>
<body>
<div class="flyer">
  <div class="hero-photo" role="img" aria-label="Photo of a driver in a hi-vis shirt standing beside a red company dump truck"></div>

  <svg class="shapes" width="848" height="1200" viewBox="0 0 848 1200" aria-hidden="true">
    <path d="M0,435 C40,505 140,548 240,552 L0,560 Z" fill="var(--green)"/>
    <path d="M0,527 C90,548 170,556 240,552 C320,520 380,470 431,450 C600,470 760,510 848,556 L848,1200 L0,1200 Z" fill="var(--white)"/>
    <path d="M431,428 C520,375 640,365 848,440 L848,456 C640,382 520,392 431,445 Z" fill="var(--green)"/>
    <path d="M431,450 C520,390 640,380 848,456 L848,556 C740,505 600,462 431,450 Z" fill="var(--yellow)"/>
    <circle cx="287" cy="418" r="146" fill="var(--green)"/>
    <circle cx="296" cy="426" r="137" fill="var(--white)"/>
    <path d="M848,880 C820,990 700,1060 520,1078 L848,1078 Z" fill="var(--green)"/>
    <path d="M0,1048 C100,1018 210,1020 330,1045 C450,1068 600,1074 848,1022 L848,1200 L0,1200 Z" fill="var(--black)"/>
  </svg>

  <div class="headline headline--hiring">HIRING</div>
  <div class="headline headline--drivers">DRIVERS</div>

  <div class="brand">
    <div class="brand__name">KORVA</div>
    <div class="brand__legal">HOLDINGS, LLC</div>
    <div class="brand__place">OAK FALLS, WI</div>
  </div>

  <section class="equipment">
    <h2 class="equipment__title">We have a variety of equipment from</h2>
    <ul class="bullets">
      <li>Dump Trucks</li>
      <li>Roll Off Trucks to Semis<br>with Belt Trailers</li>
      <li>Walking Floors</li>
      <li>Gondolas</li>
      <li>Tankers</li>
      <li>Vans and Compacting Trailers</li>
    </ul>
  </section>
  <p class="note equipment__note">We haul various materials from general aggregate freight to various types of non-hazardous wastes such as garbage, recyclables, paper mill sludge, metal, shredder fluff to various landfills or recycling centers.</p>

  <section class="perks">
    <h2 class="perks__title">WHY CHOOSE <strong>US!</strong></h2>
    <ul class="bullets">
      <li>Great Pay</li>
      <li>Sign on Bonus</li>
      <li>Holiday &amp; Vacation Pay</li>
      <li>Health Insurance, Vision &amp;<br>Dental Offered</li>
      <li>Tankers</li>
      <li>Employer Paid Life Insurance</li>
      <li>Uniforms</li>
      <li>Phone Reimbursement</li>
      <li>PLUMEX</li>
    </ul>
  </section>
  <p class="note perks__note perks__note--pay" style="text-align:left">Rate of pay is based on experience and the variety of equipment you are able to operate or your willingness to learn.</p>
  <p class="note perks__note perks__note--home">All work is local and you are home every night.</p>

  <footer class="footer">
    <div class="footer__call">CALL US +00 123 456 789</div>
    <div class="footer__social">@Socialmedia / 0123 456 789</div>
    <div class="footer__icons">
      <span class="footer__icon"></span>
      <span class="footer__icon"></span>
      <span class="footer__icon">
        <svg width="18" height="18" viewBox="0 0 24 24" aria-hidden="true"><path d="M6.6 10.8a15.1 15.1 0 0 0 6.6 6.6l2.2-2.2a1 1 0 0 1 1-.25 11.4 11.4 0 0 0 3.6.57 1 1 0 0 1 1 1V20a1 1 0 0 1-1 1A17 17 0 0 1 3 4a1 1 0 0 1 1-1h3.5a1 1 0 0 1 1 1c0 1.25.2 2.45.57 3.57a1 1 0 0 1-.25 1z" fill="#000"/></svg>
      </span>
    </div>
  </footer>
</div>
</body>
</html>
```